Career Counselor in need of a business card design

Hello Creatives! I'm in need of a business card design for a new company based in Georgia, USA called Pathways By Lantern.

Some things that may be helpful in creating your concept(s) include:

My Logo (Included in the Files section): There are three versions, two versions are in the second file. The all gold stacked (vertical) version is my primary logo and then there are two horizontal versions (one is all gold and the other is gold and grey).

My mission: to empower tweens through young adults to realize and actualize their CAREER ASPIRATIONS.
My vision: for tweens through young adults to LIVE LIFE ON PURPOSE and become CONTRIBUTING MEMBERS OF SOCIETY.

Biblical scriptures that support my ‘Why’: Psalms 127: 3-4(NIV) Children are a heritage from the Lord, offspring a reward from him. Like ARROWS in the hands of a warrior are children…. And Proverbs 29:18(JKV) Where there is no VISION, the people perish.

*Words in ALL CAPS are to emphasize what's important to me and may possibly provide you some inspiration (IDK - Have fun with it)!

Target Market(s)

My ideal customers are parents, guardians, and young adults.

Contact Information for Business Card

My name, degrees and credential: Delphine Marlow, M.S., Ed.S., NCC
Title: College and Career Coach and Consultant

Number: 555.318.2907
Address: 2718 Willowmere Avenue., Suite 405, Macon, GA 31299
Email: info@pathwaysbylantern.example
Website: www.pathwaysbylantern.example

My population: TWEENS • TEENS • EMERGING ADULTS
Services offered: One-On-One Sessions • Small Groups • Workshops

Colors

Designer to choose colors to be used in the design.

Requirements
Nice to have
• Either my mission or vision but I will understand if it does not all fit.
• My mission: To empower tweens through young adults to realize and actualize their career aspirations.
• My vision: For tweens through young adults to live life on purpose and become contributing members of society.

```html
<!DOCTYPE html>
<html lang="en">
<head>
<meta charset="utf-8">
<title>Pathways By Lantern — Business Card</title>
<link href="https://fonts.googleapis.com/css2?family=PT+Sans:wght@400;700&display=swap" rel="stylesheet">
<style>
  :root {
    --backdrop: #3b3c3f;
    --card: #1c1c1e;
    --gold: #cfa738;
    --gold-soft: #b8922c;
    --ink-light: #e9e6df;
    --ghost: #2b2a28;
  }
  * { margin: 0; padding: 0; box-sizing: border-box; }
  html, body {
    width: 1200px; height: 1200px; overflow: hidden;
    background: var(--backdrop);
    font-family: "PT Sans", sans-serif;
  }
  .canvas { position: relative; width: 1200px; height: 1200px; }
  .card {
    position: absolute; left: 160px;
    width: 880px; height: 503px;
    background: var(--card);
    overflow: hidden;
  }
  .card--front { top: 60px; }
  .card--back { top: 597px; }

  /* brand lockup */
  .brand { display: flex; flex-direction: column; align-items: center; }
  .brand__mark {
    width: 92px; height: 92px; border-radius: 50%;
    border: 5px solid var(--gold);
  }
  .brand__name {
    margin-top: 14px;
    color: var(--gold); font-weight: 700;
    font-size: 34px; letter-spacing: 1px; white-space: nowrap;
  }

  /* front */
  .front__brand { position: absolute; left: 0; right: 0; top: 110px; }
  .front__tagline {
    position: absolute; left: 0; right: 0; top: 350px;
    text-align: center; color: var(--gold);
    font-size: 17px; line-height: 1.6; letter-spacing: .3px;
  }

  /* back */
  .back__brand { position: absolute; left: 70px; top: 52px; }
  .back__brand .brand__mark { width: 80px; height: 80px; }
  .back__brand .brand__name { font-size: 30px; }
  .back__ghost {
    position: absolute; right: -40px; top: 40px;
    width: 380px; height: 380px; border-radius: 50%;
    border: 26px solid var(--ghost);
  }
  .person {
    position: absolute; left: 0; top: 262px;
    display: flex; align-items: stretch;
  }
  .person__bar { width: 14px; background: var(--gold); margin-right: 30px; }
  .person__name {
    color: var(--gold); font-weight: 700; font-size: 27px; letter-spacing: .5px;
  }
  .person__creds { color: var(--ink-light); font-weight: 400; font-size: 19px; margin-left: 6px; letter-spacing: 0; }
  .person__title { color: var(--ink-light); font-size: 20px; margin-top: 2px; }

  .contact {
    position: absolute; left: 96px; top: 362px;
    list-style: none; color: var(--ink-light); font-size: 19px;
  }
  .contact__item { display: flex; align-items: center; height: 30px; }
  .contact__icon { width: 16px; height: 16px; margin-right: 12px; fill: var(--gold-soft); }

  .address {
    position: absolute; right: 50px; top: 230px;
    text-align: right; color: var(--ink-light); font-size: 19px; line-height: 1.45;
  }
</style>
</head>
<body>
<main class="canvas">

  <section class="card card--front" aria-label="Card front">
    <div class="brand front__brand">
      <div class="brand__mark"></div>
      <div class="brand__name">Pathways By Lantern</div>
    </div>
    <p class="front__tagline">
      “TWEENS • TEENS • EMERGING ADULTS”<br>
      Services : One-On-One Sessions • Small Groups • Workshops
    </p>
  </section>

  <section class="card card--back" aria-label="Card back">
    <div class="back__ghost" aria-hidden="true"></div>

    <div class="brand back__brand">
      <div class="brand__mark"></div>
      <div class="brand__name">Pathways By Lantern</div>
    </div>

    <div class="person">
      <div class="person__bar"></div>
      <div>
        <div class="person__name">DELPHINE MARLOW<span class="person__creds">M.S., ED.S., NCC</span></div>
        <div class="person__title">College &amp; Career Coach &amp; Consultant</div>
      </div>
    </div>

    <ul class="contact">
      <li class="contact__item">
        <svg class="contact__icon" viewBox="0 0 16 16"><path d="M3.5 1l2.6 2.8-1.3 2a8 8 0 0 0 5.4 5.4l2-1.3L15 12.5l-2 2.3C7 14.5 1.5 9 1.2 3z"/></svg>
        555.318.2907
      </li>
      <li class="contact__item">
        <svg class="contact__icon" viewBox="0 0 16 16"><path d="M1 3h14v10H1z M1.8 3.6L8 8.6l6.2-5" stroke="#1c1c1e" stroke-width="1.3"/></svg>
        info@pathwaysbylantern.example
      </li>
      <li class="contact__item">
        <svg class="contact__icon" viewBox="0 0 16 16"><circle cx="8" cy="8" r="7"/><path d="M1 8h14M8 1c-3 3.5-3 10.5 0 14M8 1c3 3.5 3 10.5 0 14" stroke="#1c1c1e" stroke-width="1.1" fill="none"/></svg>
        www.pathwaysbylantern.example
      </li>
    </ul>

    <p class="address">
      2718 Willowmere Avenue<br>
      Suite 405, Macon, GA 31299
    </p>
  </section>

</main>
</body>
</html>
```